" Fazer o calendário de parede conforme o anexo abaixo sendo que a parte para fazer o cabeçalho tem que ter a medida 41cm de comprimento por 11,5cm de altura "

```html
<!DOCTYPE html>
<html lang="pt-BR">
<head>
<meta charset="UTF-8">
<title>Calendário de Parede – Pomar Verde Hortifruti</title>
<link rel="stylesheet" href="https://fonts.googleapis.com/css2?family=Montserrat:wght@400;600;700&display=swap">
<style>
  :root{
    --bg:#e8ebe4;
    --paper:#ffffff;
    --orange:#f08a24;
    --orange-soft:#fbe0c4;
    --green:#1f5a2a;
    --ink:#4a4a4a;
    --muted:#8a8a8a;
  }
  *{margin:0;padding:0;box-sizing:border-box}
  html,body{width:1200px;height:1200px;overflow:hidden}
  body{background:var(--bg);font-family:"Montserrat",sans-serif;color:var(--ink);position:relative}
  .calendar{position:absolute;left:50px;top:166px;width:1100px;height:868px;background:var(--paper);box-shadow:0 6px 24px rgba(0,0,0,.12)}
  .header{position:relative;width:1100px;height:308px;overflow:hidden}
  .header-photo{position:absolute;inset:0;background:
      radial-gradient(circle at 70% 35%,#ffb347 0,#f7941d 30%,transparent 60%),
      radial-gradient(circle at 20% 80%,#e86a12 0,transparent 45%),
      linear-gradient(120deg,#3f7a2a 0%,#f08a24 35%,#f6a53a 65%,#d9651a 100%)}
  .brand{position:absolute;left:60px;top:50%;transform:translateY(-50%);display:flex;align-items:center;gap:18px}
  .brand-dot{width:34px;height:34px;border-radius:50%;background:var(--paper)}
  .brand-name{font-weight:700;font-size:44px;line-height:1.05;color:var(--paper)}
  .months{display:grid;grid-template-columns:repeat(4,1fr);grid-template-rows:repeat(3,1fr);height:560px;padding:34px 40px 30px;gap:24px 30px}
  .month{display:flex;gap:8px}
  .month-name{writing-mode:vertical-rl;transform:rotate(180deg);font-size:14px;font-weight:600;color:var(--ink);text-align:center}
  .month-body{flex:1}
  .weekdays{display:grid;grid-template-columns:repeat(7,1fr);background:var(--orange);color:var(--paper);font-size:9px;font-weight:700;text-align:center;height:16px;line-height:16px;border-radius:2px;margin-bottom:4px}
  .days{display:grid;grid-template-columns:repeat(7,1fr);grid-auto-rows:20px;font-size:11px;text-align:center;line-height:20px}
  .days i{font-style:normal}
  .days i:nth-child(7n+1){color:var(--orange)}
  .s1{grid-column-start:2}.s2{grid-column-start:3}.s3{grid-column-start:4}
  .s4{grid-column-start:5}.s5{grid-column-start:6}.s6{grid-column-start:7}
</style>
</head>
<body>
<main class="calendar">
  <header class="header">
    <div class="header-photo" role="img" aria-label="Fotografia de laranjas e frutas cítricas frescas com folhas verdes"></div>
    <div class="brand"><span class="brand-dot"></span><span class="brand-name">Pomar Verde<br>Hortifruti</span></div>
  </header>
  <section class="months">
    <div class="month"><div class="month-name">Janeiro</div><div class="month-body"><div class="weekdays"><span>D</span><span>S</span><span>T</span><span>Q</span><span>Q</span><span>S</span><span>S</span></div><div class="days"><i class="s3">1</i><i>2</i><i>3</i><i>4</i><i>5</i><i>6</i><i>7</i><i>8</i><i>9</i><i>10</i><i>11</i><i>12</i><i>13</i><i>14</i><i>15</i><i>16</i><i>17</i><i>18</i><i>19</i><i>20</i><i>21</i><i>22</i><i>23</i><i>24</i><i>25</i><i>26</i><i>27</i><i>28</i><i>29</i><i>30</i><i>31</i></div></div></div>
    <div class="month"><div class="month-name">Fevereiro</div><div class="month-body"><div class="weekdays"><span>D</span><span>S</span><span>T</span><span>Q</span><span>Q</span><span>S</span><span>S</span></div><div class="days"><i class="s6">1</i><i>2</i><i>3</i><i>4</i><i>5</i><i>6</i><i>7</i><i>8</i><i>9</i><i>10</i><i>11</i><i>12</i><i>13</i><i>14</i><i>15</i><i>16</i><i>17</i><i>18</i><i>19</i><i>20</i><i>21</i><i>22</i><i>23</i><i>24</i><i>25</i><i>26</i><i>27</i><i>28</i></div></div></div>
    <div class="month"><div class="month-name">Março</div><div class="month-body"><div class="weekdays"><span>D</span><span>S</span><span>T</span><span>Q</span><span>Q</span><span>S</span><span>S</span></div><div class="days"><i class="s6">1</i><i>2</i><i>3</i><i>4</i><i>5</i><i>6</i><i>7</i><i>8</i><i>9</i><i>10</i><i>11</i><i>12</i><i>13</i><i>14</i><i>15</i><i>16</i><i>17</i><i>18</i><i>19</i><i>20</i><i>21</i><i>22</i><i>23</i><i>24</i><i>25</i><i>26</i><i>27</i><i>28</i><i>29</i><i>30</i><i>31</i></div></div></div>
    <div class="month"><div class="month-name">Abril</div><div class="month-body"><div class="weekdays"><span>D</span><span>S</span><span>T</span><span>Q</span><span>Q</span><span>S</span><span>S</span></div><div class="days"><i class="s2">1</i><i>2</i><i>3</i><i>4</i><i>5</i><i>6</i><i>7</i><i>8</i><i>9</i><i>10</i><i>11</i><i>12</i><i>13</i><i>14</i><i>15</i><i>16</i><i>17</i><i>18</i><i>19</i><i>20</i><i>21</i><i>22</i><i>23</i><i>24</i><i>25</i><i>26</i><i>27</i><i>28</i><i>29</i><i>30</i></div></div></div>
    <div class="month"><div class="month-name">Maio</div><div class="month-body"><div class="weekdays"><span>D</span><span>S</span><span>T</span><span>Q</span><span>Q</span><span>S</span><span>S</span></div><div class="days"><i class="s4">1</i><i>2</i><i>3</i><i>4</i><i>5</i><i>6</i><i>7</i><i>8</i><i>9</i><i>10</i><i>11</i><i>12</i><i>13</i><i>14</i><i>15</i><i>16</i><i>17</i><i>18</i><i>19</i><i>20</i><i>21</i><i>22</i><i>23</i><i>24</i><i>25</i><i>26</i><i>27</i><i>28</i><i>29</i><i>30</i><i>31</i></div></div></div>
    <div class="month"><div class="month-name">Junho</div><div class="month-body"><div class="weekdays"><span>D</span><span>S</span><span>T</span><span>Q</span><span>Q</span><span>S</span><span>S</span></div><div class="days"><i>1</i><i>2</i><i>3</i><i>4</i><i>5</i><i>6</i><i>7</i><i>8</i><i>9</i><i>10</i><i>11</i><i>12</i><i>13</i><i>14</i><i>15</i><i>16</i><i>17</i><i>18</i><i>19</i><i>20</i><i>21</i><i>22</i><i>23</i><i>24</i><i>25</i><i>26</i><i>27</i><i>28</i><i>29</i><i>30</i></div></div></div>
    <div class="month"><div class="month-name">Julho</div><div class="month-body"><div class="weekdays"><span>D</span><span>S</span><span>T</span><span>Q</span><span>Q</span><span>S</span><span>S</span></div><div class="days"><i class="s2">1</i><i>2</i><i>3</i><i>4</i><i>5</i><i>6</i><i>7</i><i>8</i><i>9</i><i>10</i><i>11</i><i>12</i><i>13</i><i>14</i><i>15</i><i>16</i><i>17</i><i>18</i><i>19</i><i>20</i><i>21</i><i>22</i><i>23</i><i>24</i><i>25</i><i>26</i><i>27</i><i>28</i><i>29</i><i>30</i><i>31</i></div></div></div>
    <div class="month"><div class="month-name">Agosto</div><div class="month-body"><div class="weekdays"><span>D</span><span>S</span><span>T</span><span>Q</span><span>Q</span><span>S</span><span>S</span></div><div class="days"><i class="s5">1</i><i>2</i><i>3</i><i>4</i><i>5</i><i>6</i><i>7</i><i>8</i><i>9</i><i>10</i><i>11</i><i>12</i><i>13</i><i>14</i><i>15</i><i>16</i><i>17</i><i>18</i><i>19</i><i>20</i><i>21</i><i>22</i><i>23</i><i>24</i><i>25</i><i>26</i><i>27</i><i>28</i><i>29</i><i>30</i><i>31</i></div></div></div>
    <div class="month"><div class="month-name">Setembro</div><div class="month-body"><div class="weekdays"><span>D</span><span>S</span><span>T</span><span>Q</span><span>Q</span><span>S</span><span>S</span></div><div class="days"><i class="s1">1</i><i>2</i><i>3</i><i>4</i><i>5</i><i>6</i><i>7</i><i>8</i><i>9</i><i>10</i><i>11</i><i>12</i><i>13</i><i>14</i><i>15</i><i>16</i><i>17</i><i>18</i><i>19</i><i>20</i><i>21</i><i>22</i><i>23</i><i>24</i><i>25</i><i>26</i><i>27</i><i>28</i><i>29</i><i>30</i></div></div></div>
    <div class="month"><div class="month-name">Outubro</div><div class="month-body"><div class="weekdays"><span>D</span><span>S</span><span>T</span><span>Q</span><span>Q</span><span>S</span><span>S</span></div><div class="days"><i class="s3">1</i><i>2</i><i>3</i><i>4</i><i>5</i><i>6</i><i>7</i><i>8</i><i>9</i><i>10</i><i>11</i><i>12</i><i>13</i><i>14</i><i>15</i><i>16</i><i>17</i><i>18</i><i>19</i><i>20</i><i>21</i><i>22</i><i>23</i><i>24</i><i>25</i><i>26</i><i>27</i><i>28</i><i>29</i><i>30</i><i>31</i></div></div></div>
    <div class="month"><div class="month-name">Novembro</div><div class="month-body"><div class="weekdays"><span>D</span><span>S</span><span>T</span><span>Q</span><span>Q</span><span>S</span><span>S</span></div><div class="days"><i class="s6">1</i><i>2</i><i>3</i><i>4</i><i>5</i><i>6</i><i>7</i><i>8</i><i>9</i><i>10</i><i>11</i><i>12</i><i>13</i><i>14</i><i>15</i><i>16</i><i>17</i><i>18</i><i>19</i><i>20</i><i>21</i><i>22</i><i>23</i><i>24</i><i>25</i><i>26</i><i>27</i><i>28</i><i>29</i><i>30</i></div></div></div>
    <div class="month"><div class="month-name">Dezembro</div><div class="month-body"><div class="weekdays"><span>D</span><span>S</span><span>T</span><span>Q</span><span>Q</span><span>S</span><span>S</span></div><div class="days"><i class="s1">1</i><i>2</i><i>3</i><i>4</i><i>5</i><i>6</i><i>7</i><i>8</i><i>9</i><i>10</i><i>11</i><i>12</i><i>13</i><i>14</i><i>15</i><i>16</i><i>17</i><i>18</i><i>19</i><i>20</i><i>21</i><i>22</i><i>23</i><i>24</i><i>25</i><i>26</i><i>27</i><i>28</i><i>29</i><i>30</i><i>31</i></div></div></div>
  </section>
</main>
</body>
</html>
```